Create a new email template des

We are looking for 2 email template designed similar to the attached supplied like Inn Quickly in order to promote of photography business and also our marketing agency.

Both similar in design and branding but with a slight change to the body area.

1. Email is to show images and a little text as attached.
2. Email is to show more text and longer emails with tips and best practices education.

Our website is: www.corvanmeadow.com

The photography site is: http://corvanmeadow.com/hotel-photography/

Target Market(s)

Luxury Hotels

Industry/Entity Type

Business

Requirements
Must have
• Stylish design and as per breif

```html
<!DOCTYPE html>
<html lang="en">
<head>
<meta charset="utf-8">
<title>Corvan Meadow – Email Template 1</title>
<link href="https://fonts.googleapis.com/css2?family=Cormorant+SC:wght@500&family=Jost:wght@400;500&family=Oswald:wght@300;400&display=swap" rel="stylesheet">
<style>
  :root{
    --ink:#1c1c1c;
    --tile-dark:#222222;
    --tile-mid:#2b2b2b;
    --header:#1d1d1d;
    --paper:#ffffff;
    --soft-grey:#ececec;
    --light-text:#dcdcdc;
    --body-text:#2a2a2a;
    --label:#111111;
  }
  *{box-sizing:border-box;margin:0;padding:0}
  html,body{width:1200px;height:1000px;overflow:hidden;background:var(--paper)}
  body{position:relative;font-family:"Jost",sans-serif}

  .board-title{position:absolute;left:57px;top:52px;font-family:"Oswald",sans-serif;font-weight:400;font-size:22px;letter-spacing:2px;color:var(--label)}

  .panel{position:absolute;overflow:hidden;background:var(--paper)}
  .panel--thumb{left:57px;top:97px;width:205px;height:862px}
  .panel--thumb .email{transform:scale(.5601);transform-origin:top left}
  .panel--top{left:368px;top:52px;width:366px;height:905px;box-shadow:14px 16px 20px rgba(0,0,0,.38)}
  .panel--bottom{left:771px;top:195px;width:366px;height:632px;box-shadow:14px 16px 20px rgba(0,0,0,.38)}
  .panel--bottom .email{margin-top:-905px}

  .email{width:366px;background:var(--paper)}

  .email-header{height:63px;background:var(--header);display:flex;align-items:center;justify-content:space-between;padding:0 21px}
  .brand{font-family:"Cormorant SC",serif;font-weight:500;font-size:16px;letter-spacing:.5px;color:#e4e4e4}
  .nav{display:flex;gap:22px;font-family:"Oswald",sans-serif;font-weight:400;font-size:11px;color:#e4e4e4;letter-spacing:.5px}

  .hero{position:relative;height:191px;background:linear-gradient(180deg,#3d4a6e 0%,#6f7c9c 45%,#4f6670 70%,#3f8a95 100%)}
  .hero-title{position:absolute;left:20px;top:46px;font-family:"Oswald",sans-serif;font-weight:300;font-size:26px;line-height:34px;color:#fff}

  .intro{height:107px;padding:20px 20px 0;text-align:center}
  .copy{font-size:7.3px;line-height:14px;text-align:justify;color:var(--body-text)}
  .button{display:inline-block;margin-top:6px;width:89px;height:19px;border:1.2px solid var(--ink);font-size:6.5px;letter-spacing:1.2px;line-height:17px;text-align:center;color:var(--ink)}

  .tile-row{display:grid;grid-template-columns:182px 184px}
  .tile-image{position:relative;height:180px}
  .tile-caption{position:absolute;left:21px;bottom:14px;color:#fff}
  .tile-caption b{display:block;font-family:"Oswald",sans-serif;font-weight:400;font-size:7px;letter-spacing:.4px}
  .tile-caption span{display:block;font-size:8px}
  .tile-text{height:92px;padding:16px 20px 0 21px;font-size:7.4px;line-height:15px;color:var(--light-text);background:var(--tile-dark)}
  .tile-row > div:nth-child(2) .tile-text{background:var(--tile-mid)}

  .photo-resort-dusk{background:linear-gradient(180deg,#2f4a8a 0%,#2b3f5c 55%,#7a5a2a 80%,#1a2030 100%)}
  .photo-terrace{background:linear-gradient(160deg,#5a6fa0 0%,#7a4a2a 45%,#3a241a 100%)}
  .photo-beach-sunset{background:linear-gradient(180deg,#c9a07a 0%,#b88068 40%,#6a4a50 75%,#2a2020 100%)}
  .photo-suite{background:linear-gradient(150deg,#8a6a40 0%,#c9a878 40%,#6a4a2c 100%)}
  .photo-dining{background:linear-gradient(160deg,#5a4a3a 0%,#3a2a22 50%,#24201c 100%)}
  .photo-mountain-pool{background:linear-gradient(180deg,#5d8ac0 0%,#a8c4de 40%,#4a6a50 70%,#2e4a58 100%)}

  .feature{height:169px;background:var(--soft-grey);padding:18px 20px 0;text-align:center}
  .feature-title{font-family:"Oswald",sans-serif;font-weight:400;font-size:20px;letter-spacing:.5px;color:var(--ink);margin-bottom:6px}
  .feature .copy{line-height:14.3px}
  .feature .button{margin-top:9px}

  .footer{position:relative;height:191px;background:linear-gradient(180deg,#1f3a7a 0%,#203055 35%,#2a2520 60%,#050505 100%)}
  .footer-details{position:absolute;left:0;right:0;top:117px;display:grid;grid-template-columns:1fr 1fr 1fr;padding:0 16px 0 36px;color:#eee}
  .footer-details div:last-child{text-align:right}
  .footer-details b{display:block;font-family:"Oswald",sans-serif;font-weight:400;font-size:5.5px;letter-spacing:.6px;margin-bottom:4px}
  .footer-details span{font-size:8px}
  .social{position:absolute;left:0;right:0;top:154px;display:flex;justify-content:center;gap:7px}
  .social span{width:13px;height:13px;border:1px solid #ddd;border-radius:50%}
</style>
</head>
<body>

<div class="board-title">TEMPLATE 1 - IMAGES</div>

<!-- Full overview -->
<div class="panel panel--thumb">
  <div class="email">
    <header class="email-header"><div class="brand">CORVAN MEADOW</div><nav class="nav"><span>LINK1</span><span>LINK2</span><span>LINK3</span></nav></header>
    <section class="hero" role="img" aria-label="Resort rooftop pool with palm trees and canopy sculptures at dusk"><h1 class="hero-title">LOREM IPSUM<br>DOLOR SIT AMET<br>CONSECTETUR</h1></section>
    <section class="intro"><p class="copy">Lorem ipsum dolor sit amet, consectetur adipiscing elit. Curabitur auctor sem in magna interdum rutrum. Quisque sit amet libero consequat. Curabitur auctor sem in magna interdum rutrum. Quisque sit amet libero consequat.</p><span class="button">CONTACT US</span></section>
    <section class="tile-row">
      <div><div class="tile-image photo-resort-dusk" role="img" aria-label="Waterside pavilion lit at dusk"><div class="tile-caption"><b>LOREM IPSUM</b><span>Dolor Sit Amet</span></div></div><p class="tile-text">Dolor sit amet, consectetur adipiscing elit. Curabitur auctor sem in magna interdum rutrum. Quisque sit amet libero consequat, facilisis neque non, egestas.</p></div>
      <div><div class="tile-image photo-terrace" role="img" aria-label="Hotel terrace walkway with torches"><div class="tile-caption"><b>LOREM IPSUM</b><span>Dolor Sit Amet</span></div></div><p class="tile-text">Dolor sit amet, consectetur adipiscing elit. Curabitur auctor sem in magna interdum rutrum. Quisque sit amet libero consequat, facilisis neque non, egestas.</p></div>
    </section>
    <section class="tile-row">
      <div><div class="tile-image photo-beach-sunset" role="img" aria-label="Beach gazebo at sunset"><div class="tile-caption"><b>LOREM IPSUM</b><span>Dolor Sit Amet</span></div></div><p class="tile-text">Dolor sit amet, consectetur adipiscing elit. Curabitur auctor sem in magna interdum rutrum. Quisque sit amet libero consequat, facilisis neque non, egestas.</p></div>
      <div><div class="tile-image photo-suite" role="img" aria-label="Luxury hotel suite bedroom"><div class="tile-caption"><b>LOREM IPSUM</b><span>Dolor Sit Amet</span></div></div><p class="tile-text">Dolor sit amet, consectetur adipiscing elit. Curabitur auctor sem in magna interdum rutrum. Quisque sit amet libero consequat, facilisis neque non, egestas.</p></div>
    </section>
    <section class="tile-row">
      <div><div class="tile-image photo-dining" role="img" aria-label="Restaurant dining room with chandelier"><div class="tile-caption"><b>LOREM IPSUM</b><span>Dolor Sit Amet</span></div></div><p class="tile-text">Dolor sit amet, consectetur adipiscing elit. Curabitur auctor sem in magna interdum rutrum. Quisque sit amet libero consequat, facilisis neque non, egestas.</p></div>
      <div><div class="tile-image photo-mountain-pool" role="img" aria-label="Infinity pool facing a mountain"><div class="tile-caption"><b>LOREM IPSUM</b><span>Dolor Sit Amet</span></div></div><p class="tile-text">Dolor sit amet, consectetur adipiscing elit. Curabitur auctor sem in magna interdum rutrum. Quisque sit amet libero consequat, facilisis neque non, egestas.</p></div>
    </section>
    <section class="feature"><h2 class="feature-title">LOREM IPSUM DOLOR SIT AMET</h2><p class="copy">Lorem ipsum dolor sit amet, consectetur adipiscing elit. Curabitur auctor sem in magna interdum rutrum. Quisque sit amet libero consequat, facilisis neque non, egestas tortor. Ut egestas mollis ornare. Pellentesque ut ultricies tellus, id rutrum nisl. Fusce ullamcorper finibus dolor ac tristique. Aenean sit amet felis eget velit sollicitudin maximus eu et ligula. Nullam sed enim vel risus finibus semper nec ac ex.</p><span class="button">CONTACT US</span></section>
    <footer class="footer" role="img" aria-label="Evening terrace restaurant with guests under palm trees">
      <div class="footer-details"><div><b>LONDON ADDRESS</b><span>1234 St., City, London</span></div><div><b>DUBAI ADDRESS</b><span>1234 St., City, Dubai</span></div><div><b>EMAIL</b><span>email@email.com</span></div></div>
      <div class="social"><span></span><span></span><span></span><span></span><span></span><span></span></div>
    </footer>
  </div>
</div>

<!-- Upper detail -->
<div class="panel panel--top">
  <div class="email">
    <header class="email-header"><div class="brand">CORVAN MEADOW</div><nav class="nav"><span>LINK1</span><span>LINK2</span><span>LINK3</span></nav></header>
    <section class="hero" role="img" aria-label="Resort rooftop pool with palm trees and canopy sculptures at dusk"><h1 class="hero-title">LOREM IPSUM<br>DOLOR SIT AMET<br>CONSECTETUR</h1></section>
    <section class="intro"><p class="copy">Lorem ipsum dolor sit amet, consectetur adipiscing elit. Curabitur auctor sem in magna interdum rutrum. Quisque sit amet libero consequat. Curabitur auctor sem in magna interdum rutrum. Quisque sit amet libero consequat.</p><span class="button">CONTACT US</span></section>
    <section class="tile-row">
      <div><div class="tile-image photo-resort-dusk" role="img" aria-label="Waterside pavilion lit at dusk"><div class="tile-caption"><b>LOREM IPSUM</b><span>Dolor Sit Amet</span></div></div><p class="tile-text">Dolor sit amet, consectetur adipiscing elit. Curabitur auctor sem in magna interdum rutrum. Quisque sit amet libero consequat, facilisis neque non, egestas.</p></div>
      <div><div class="tile-image photo-terrace" role="img" aria-label="Hotel terrace walkway with torches"><div class="tile-caption"><b>LOREM IPSUM</b><span>Dolor Sit Amet</span></div></div><p class="tile-text">Dolor sit amet, consectetur adipiscing elit. Curabitur auctor sem in magna interdum rutrum. Quisque sit amet libero consequat, facilisis neque non, egestas.</p></div>
    </section>
    <section class="tile-row">
      <div><div class="tile-image photo-beach-sunset" role="img" aria-label="Beach gazebo at sunset"><div class="tile-caption"><b>LOREM IPSUM</b><span>Dolor Sit Amet</span></div></div><p class="tile-text">Dolor sit amet, consectetur adipiscing elit. Curabitur auctor sem in magna interdum rutrum. Quisque sit amet libero consequat, facilisis neque non, egestas.</p></div>
      <div><div class="tile-image photo-suite" role="img" aria-label="Luxury hotel suite bedroom"><div class="tile-caption"><b>LOREM IPSUM</b><span>Dolor Sit Amet</span></div></div><p class="tile-text">Dolor sit amet, consectetur adipiscing elit. Curabitur auctor sem in magna interdum rutrum. Quisque sit amet libero consequat, facilisis neque non, egestas.</p></div>
    </section>
  </div>
</div>

<!-- Lower detail -->
<div class="panel panel--bottom">
  <div class="email">
    <div style="height:905px"></div>
    <section class="tile-row">
      <div><div class="tile-image photo-dining" role="img" aria-label="Restaurant dining room with chandelier"><div class="tile-caption"><b>LOREM IPSUM</b><span>Dolor Sit Amet</span></div></div><p class="tile-text">Dolor sit amet, consectetur adipiscing elit. Curabitur auctor sem in magna interdum rutrum. Quisque sit amet libero consequat, facilisis neque non, egestas.</p></div>
      <div><div class="tile-image photo-mountain-pool" role="img" aria-label="Infinity pool facing a mountain"><div class="tile-caption"><b>LOREM IPSUM</b><span>Dolor Sit Amet</span></div></div><p class="tile-text">Dolor sit amet, consectetur adipiscing elit. Curabitur auctor sem in magna interdum rutrum. Quisque sit amet libero consequat, facilisis neque non, egestas.</p></div>
    </section>
    <section class="feature"><h2 class="feature-title">LOREM IPSUM DOLOR SIT AMET</h2><p class="copy">Lorem ipsum dolor sit amet, consectetur adipiscing elit. Curabitur auctor sem in magna interdum rutrum. Quisque sit amet libero consequat, facilisis neque non, egestas tortor. Ut egestas mollis ornare. Pellentesque ut ultricies tellus, id rutrum nisl. Fusce ullamcorper finibus dolor ac tristique. Aenean sit amet felis eget velit sollicitudin maximus eu et ligula. Nullam sed enim vel risus finibus semper nec ac ex.</p><span class="button">CONTACT US</span></section>
    <footer class="footer" role="img" aria-label="Evening terrace restaurant with guests under palm trees">
      <div class="footer-details"><div><b>LONDON ADDRESS</b><span>1234 St., City, London</span></div><div><b>DUBAI ADDRESS</b><span>1234 St., City, Dubai</span></div><div><b>EMAIL</b><span>email@email.com</span></div></div>
      <div class="social"><span></span><span></span><span></span><span></span><span></span><span></span></div>
    </footer>
  </div>
</div>

</body>
</html>
```